Homepage für Unternehmensberatung
Zielgruppe
Wir sind eine Unternehmensberatung mit einem klaren Branchenfokus auf Banken / Finanzdienstleister.
Unsere Dienstleistungsprodukte lassen sich grob in folgende Themencluster unterteilen:
1)Strategieentwicklung
o IT-Strategie, IT-Architektur, IT-Bebauungsplan
2) Projektmanagement
o Projektportfoliomgmt., Programmmgmt., Projektmanagement, Projektcontrolling
3) Fachberatung
o Bankfachliche IT- Beratung mit Schwerpunkten Kredit, Wertpapiergeschäft,
Bankenaufsichtsrecht, Liquiditätsmanagement
o Anforderungsmanagement inkl. Aufbau von Bewertungs- und Priorisierungsmethoden
4) Prozessberatung/-optimierung
o Prozessanalyse, Prozessdesign, Prozessdokumentation
o Prozessoptimierung auf Basis etablierter Messmethoden
Unser Firmenname Lotsenwerk hat für uns eine Doppelbedeutung:
1. Im Außenverhältnis: Wir verstehen uns als Lotsenwerk unserer Kunden
2. Im Innenverhältnis: Wir pflegen einen partnerschaftlichen Umgang mit unseren
Mitarbeitern (Teamarbeit)
Aktuell sind wir ein kleines aber feines Team von erfahrenen und hochmotivierten Kollegen. Unsere Mitarbeiter sind ehemalige Führungskräfte sowie erfahrenen Unternehmensberater.
Aufgabenstellung
Entwurf / Design von 2 Seiten:
1. Seite / Startseite:
Simple und elegante Darstellung der oben genannten 4 Themencluster (z.B. Bild/Piktogramm, Textkasten) sowie einer Navigationsmöglichkeit zu folgenden Detailsichten:
• Unternehmen
• Beratungsangebot (siehe Themencluster)
• Partnerunternehmen
• Kontakt
2. Seite / 2. Ebene:
Entwurf einer Möglichkeit zur Erläuterung/Darstellung von Inhalten der Startseite.
Die Themencluster sollten auf jeder Ebene immer „anklickbar“/ zu sehen sein.
Logo
Das angehängte Logo ist in die Website einzubinden. Stil und Farben sollen übernommen werden bzw. sind Basis für das Design.
Lizenzen
Lizenz für eingesetzte Fotos und Illustrationen soll enthalten / Open-Source sein. Wenn nicht dann bitte zusätzliche Kosten angeben.

```html
<!DOCTYPE html>
<html lang="en">
<head>
<meta charset="utf-8">
<title>Lotsenwerk – Consulting</title>
<link rel="stylesheet" href="https://fonts.googleapis.com/css2?family=Open+Sans:wght@400;600;700&family=Roboto+Condensed:wght@700&display=swap">
<style>
  :root {
    --blue: #1a7fc0;
    --blue-light: #2a92d4;
    --blue-dark: #136aa3;
    --page-bg: #1f2326;
    --header-gray: #5a6167;
    --nav-bg: #3b3f43;
    --panel: rgba(70, 72, 75, 0.82);
    --text-light: #e6e8ea;
    --text-muted: #c9cdd0;
    --brand-text: #34393e;
  }
  * { box-sizing: border-box; margin: 0; padding: 0; }
  html, body { width: 1200px; height: 789px; overflow: hidden; }
  body {
    position: relative;
    background: var(--page-bg);
    font-family: "Open Sans", Arial, sans-serif;
    color: var(--text-light);
    border-top: 2px solid var(--blue);
    border-bottom: 2px solid var(--blue);
  }
  .hero-photo {
    position: absolute; left: 0; top: 0; width: 1200px; height: 671px;
    background:
      radial-gradient(ellipse 420px 300px at 600px 140px, #77797c 0%, rgba(90,92,95,0.5) 45%, rgba(30,30,32,0) 100%),
      radial-gradient(ellipse 300px 220px at 590px 520px, rgba(150,110,85,0.55) 0%, rgba(60,50,45,0) 100%),
      linear-gradient(90deg, #222426 0%, #3b3d40 25%, #4a4b4d 50%, #5b5d60 78%, #6d7073 100%);
  }
  .site-header {
    position: absolute; left: 181px; top: 24px; width: 841px; height: 60px;
    background: var(--header-gray);
  }
  .brand {
    position: absolute; left: 0; top: 0; width: 281px; height: 60px;
    background: #fff; display: flex; align-items: center; padding-left: 22px;
  }
  .brand-name { font-size: 22px; font-weight: 600; color: var(--brand-text); letter-spacing: 1px; line-height: 1; }
  .main-nav {
    position: absolute; left: 368px; top: 17px; height: 30px; width: 458px;
    background: var(--nav-bg); display: flex;
  }
  .main-nav a {
    display: flex; align-items: center; padding: 0 14px;
    font-size: 11px; font-weight: 600; color: #fff; text-decoration: none;
  }
  .main-nav a.active { background: var(--blue); padding: 0 16px; }
  .service {
    position: absolute; width: 316px; height: 79px;
    background: rgba(70,72,75,0.45); border: 1px solid rgba(120,122,125,0.55);
  }
  .service-inner {
    position: absolute; left: 10px; top: 8px; width: 295px; height: 62px;
    background: linear-gradient(180deg, var(--blue-light), var(--blue-dark));
    display: flex; align-items: center;
  }
  .service-icon {
    width: 55px; height: 100%; display: flex; align-items: center; justify-content: center;
    border-right: 1px solid rgba(255,255,255,0.25); flex: none;
  }
  .service-title {
    flex: 1; text-align: center; font-family: "Roboto Condensed", "Arial Narrow", sans-serif;
    font-weight: 700; font-size: 20px; line-height: 24px; color: #fff; letter-spacing: 0.3px;
  }
  .who-we-are {
    position: absolute; left: 181px; top: 567px; width: 841px; height: 104px;
    background: var(--panel); padding: 9px 30px 0;
  }
  .who-we-are h2 { font-size: 15px; font-weight: 400; color: #fff; margin-bottom: 5px; }
  .who-we-are p { font-size: 10.9px; line-height: 19px; color: var(--text-muted); letter-spacing: -0.05px; }
  .site-footer {
    position: absolute; left: 181px; top: 671px; width: 841px; height: 43px;
    background: var(--blue); display: flex; align-items: center; padding-left: 28px;
  }
  .footer-nav a { font-size: 11px; font-weight: 600; color: #fff; text-decoration: none; margin-right: 29px; }
  .social { margin-left: auto; margin-right: 13px; display: flex; gap: 7px; }
  .social span { width: 22px; height: 22px; border-radius: 50%; background: #3d4247; border: 1px solid #5a6066; }
  .copyright {
    position: absolute; right: 178px; top: 726px; font-size: 11.3px; color: #f0f0f0;
  }
</style>
</head>
<body>
  <div class="hero-photo" role="img" aria-label="Photo of a business team standing with arms crossed behind a close-up handshake"></div>

  <header class="site-header">
    <div class="brand">
      <div class="brand-name">LOTSENWERK</div>
    </div>
    <nav class="main-nav">
      <a class="active" href="#">COMPANY</a>
      <a href="#">CONSULTING SERVICE</a>
      <a href="#">PARTNER COMPANIES</a>
      <a href="#">CONTACT</a>
    </nav>
  </header>

  <section class="services">
    <div class="service" style="left:265px;top:297px">
      <div class="service-inner">
        <div class="service-icon">
          <svg width="32" height="32" viewBox="0 0 32 32"><circle cx="16" cy="16" r="13" fill="none" stroke="#fff" stroke-width="3"/><path d="M22 10 L13 14 L10 22 L19 18 Z" fill="#fff"/><circle cx="16" cy="16" r="2" fill="#1a7fc0"/></svg>
        </div>
        <div class="service-title">STRATEGY DEVELOPMENT</div>
      </div>
    </div>
    <div class="service" style="left:596px;top:297px">
      <div class="service-inner">
        <div class="service-icon">
          <svg width="40" height="30" viewBox="0 0 40 30" fill="#fff"><rect x="15" y="1" width="10" height="7" rx="1"/><rect x="19" y="8" width="2" height="6"/><rect x="5" y="13" width="30" height="2"/><rect x="5" y="13" width="2" height="8"/><rect x="19" y="13" width="2" height="8"/><rect x="33" y="13" width="2" height="8"/><rect x="1" y="21" width="10" height="7" rx="1"/><rect x="15" y="21" width="10" height="7" rx="1"/><rect x="29" y="21" width="10" height="7" rx="1"/></svg>
        </div>
        <div class="service-title">PROJECT MANAGEMENT</div>
      </div>
    </div>
    <div class="service" style="left:265px;top:391px">
      <div class="service-inner">
        <div class="service-icon">
          <svg width="30" height="40" viewBox="0 0 30 40" fill="none" stroke="#fff" stroke-width="2.5"><path d="M15 3 a11 11 0 0 1 6 20 v5 h-12 v-5 a11 11 0 0 1 6-20 z"/><path d="M10 32 h10 M11 36 h8"/><circle cx="12" cy="13" r="3" fill="#fff" stroke="none"/><circle cx="18" cy="15" r="2.5" fill="#fff" stroke="none"/></svg>
        </div>
        <div class="service-title">PROFESSIONAL<br>CONSULTING SERVICES</div>
      </div>
    </div>
    <div class="service" style="left:596px;top:391px">
      <div class="service-inner">
        <div class="service-icon">
          <svg width="32" height="32" viewBox="0 0 32 32" fill="none" stroke="#fff" stroke-width="3.5"><path d="M26 13 A10 10 0 0 0 8 9"/><path d="M6 19 A10 10 0 0 0 24 23"/><path d="M4 4 v8 h8" stroke-width="3"/><path d="M28 28 v-8 h-8" stroke-width="3"/></svg>
        </div>
        <div class="service-title">PROCESS CONSULTING<br>AND OPTIMIZATION</div>
      </div>
    </div>
  </section>

  <section class="who-we-are">
    <h2>WHO WE ARE</h2>
    <p>Lorem ipsum dolor sit amet, consectetuer adipiscing elit, sed diam nonummy nibh euismod tincidunt ut laoreet dolore magna aliquam erat volutpat.<br>Ut wisi enim ad minim veniam, quis nostrud exerci tation ullamcorper suscipit lobortis nisl ut aliquip ex ea commodo consequat. Duis autem vel eum<br>iriure dolor in hendrerit in vulputate velit esse molestie consequat.</p>
  </section>

  <footer class="site-footer">
    <nav class="footer-nav">
      <a href="#">COMPANY</a>
      <a href="#">CONSULTING SERVICE</a>
      <a href="#">PARTNER COMPANIES</a>
      <a href="#">CONTACT</a>
    </nav>
    <div class="social" aria-label="Social links">
      <span></span><span></span><span></span><span></span><span></span>
    </div>
  </footer>
  <div class="copyright">Copyright 2014. All rights reserved.</div>
</body>
</html>
```